Letterhead Creation

I would like to create a letterhead incorporating my family crest attached. My current letterhead with my information is also attached. I would also like to add my Paralegal Rosalind Merriweather

```html
<!DOCTYPE html>
<html lang="en">
<head>
<meta charset="utf-8">
<title>Letterhead – Law Offices of Harlan B. Whitcombe</title>
<link href="https://fonts.googleapis.com/css2?family=Didact+Gothic&family=Lato:wght@400;700&display=swap" rel="stylesheet">
<style>
  :root {
    --stage-bg: #e4e8ea;
    --paper: #ffffff;
    --cover-paper: #efeff0;
    --brand-blue: #1d3f9a;
    --crest-blue: #2a4fae;
    --crest-light: #dfe3ee;
    --body-text: #4d4d4d;
    --rule: #8a8a8a;
    --contact-text: #555555;
  }
  * { box-sizing: border-box; margin: 0; padding: 0; }
  html, body { width: 1200px; height: 784px; overflow: hidden; }
  body {
    background: radial-gradient(ellipse at 60% 40%, #eef1f2 0%, var(--stage-bg) 100%);
    position: relative;
    font-family: "Didact Gothic", sans-serif;
  }
  .sheet {
    position: absolute;
    top: 45px;
    width: 513px;
    height: 696px;
    border-radius: 14px;
    overflow: hidden;
    box-shadow: 0 2px 6px rgba(0,0,0,.18);
  }
  .sheet--letter { left: 42px; background: var(--paper); }
  .sheet--cover { left: 634px; background: var(--cover-paper); }

  .crest-small {
    position: absolute; left: 44px; top: 10px; width: 86px; height: 93px;
    background: radial-gradient(ellipse at 50% 55%, var(--crest-blue) 0%, #5a74bd 55%, var(--crest-light) 100%);
    border-radius: 40% 40% 50% 50%;
  }
  .contact {
    position: absolute; right: 42px; top: 40px;
    list-style: none; text-align: right;
    font-family: "Lato", sans-serif; font-size: 7px; color: var(--contact-text);
  }
  .contact li { height: 14.7px; display: flex; justify-content: flex-end; align-items: center; gap: 5px; }
  .contact svg { width: 8px; height: 8px; fill: var(--brand-blue); }
  .contact .address { color: var(--brand-blue); font-weight: 700; }
  .header-rule { position: absolute; left: 44px; top: 110px; width: 426px; height: 2px; background: var(--rule); }

  .crest-watermark {
    position: absolute; left: 110px; top: 195px; width: 290px; height: 420px;
    background: radial-gradient(ellipse at 50% 55%, rgba(42,79,174,.09) 0%, rgba(42,79,174,.03) 60%, rgba(42,79,174,0) 100%);
  }
  .letter-body {
    position: absolute; left: 44px; top: 134px; width: 426px;
    font-size: 11.4px; line-height: 18.6px; color: var(--body-text);
    text-align: justify; hyphens: auto;
  }
  .letter-body p + p { margin-top: 18.6px; }
  .signature { position: absolute; left: 381px; top: 580px; }
  .signature .name { font-size: 14.5px; color: #333; }
  .signature .role { font-family: "Lato", sans-serif; font-size: 9.5px; color: #444; margin-top: 5px; }

  .footer-band {
    position: absolute; left: 0; bottom: 0; width: 100%; height: 31px;
    background: var(--brand-blue); color: #fff;
    font-family: "Lato", sans-serif; font-weight: 700; font-size: 10px; letter-spacing: 2.3px;
    display: flex; align-items: center; justify-content: center;
  }

  .crest-large {
    position: absolute; left: 108px; top: 150px; width: 304px; height: 320px;
    background: radial-gradient(ellipse at 50% 58%, var(--crest-blue) 0%, #6b84c6 50%, var(--cover-paper) 78%);
  }
  .cover-firm {
    position: absolute; left: 0; top: 643px; width: 100%; text-align: center;
    font-family: "Lato", sans-serif; font-size: 10.5px; letter-spacing: 2.4px; color: var(--brand-blue);
  }
</style>
</head>
<body>
  <section class="sheet sheet--letter">
    <div class="crest-small" role="img" aria-label="Family crest"></div>
    <ul class="contact">
      <li>(555) 201-4418 <svg viewBox="0 0 10 10"><path d="M1 3c0-2 8-2 8 0v1H7V3H3v1H1zM2 5h6l1 4H1z"/></svg></li>
      <li>(555) 201-0603 <svg viewBox="0 0 10 10"><path d="M3 1h4v2H3zM1 4h8v4H7v1H3V8H1z"/></svg></li>
      <li>harlan@whitcombelaw.com <svg viewBox="0 0 10 10"><path d="M1 2h8v6H1zM1.5 2.5 5 5.5l3.5-3"/></svg></li>
      <li class="address">412 N. Alder Ave. Glendora, Ca 91740</li>
    </ul>
    <div class="header-rule"></div>

    <div class="crest-watermark" role="img" aria-label="Faint family crest watermark"></div>
    <div class="letter-body">
      <p>Lorem ipsum dolor sit amet, consectetur adipiscing elit. Donec orci purus, luctus vitae dignissim eu, iaculis sed purus. Vivamus faucibus, ipsum nec aliquet viverra, leo mauris condimentum ligula, sit amet sagittis enim ligula quis arcu. Nam egestas tortor id nisi porttitor mattis. In tortor ante, ultricies in suscipit a, tempus non massa. Vivamus et auctor mi. Fusce vel massa nulla. Phasellus nec eros mauris, et scelerisque orci. Donec malesuada orci vitae nulla accumsan porta a id massa.</p>
      <p>Quisque accumsan iaculis magna sit amet fringilla. Maecenas consequat, magna eget tincidunt semper, odio nibh rutrum mi, id feugiat ante nisi eu risus. Vestibulum nunc orci, rhoncus a placerat in, ultricies in mi. Cras mattis varius eros, vel fringilla nisi suscipit eget. Quisque scelerisque sagittis nulla at porttitor. Mauris a justo et tellus interdum tristique. Sed id augue vitae urna euismod commodo aliquet a quam. Pellentesque arcu velit, cursus et malesuada ut, consequat et diam. Nullam erat sem, rhoncus id ullamcorper vitae, rhoncus et arcu. In ultricies ultricies nulla,</p>
      <p>Kut rutrum nisi iaculis at. Donec eu magna a metus ornare faucibus. Fusce aliquet faucibus ultricies. Morbi semper, est id tincidunt gravida, sem arcu adipiscing lacus, ac bibendum nulla leo eu purus. Quisque nec diam sed risus consectetur a ccumsan quis quis nibh. Vestibulum id purus lorem. Donec eu magna a metus ornare faucibus. Fusce aliquet faucibus ultricies. Morbi semper, est id tincidunt gravida, sem arcu adipiscing lacus, ac bibendum nulla leo eu purus. Quisque nec diam sed risus consectetur a ccumsan quis quis nibh. Vestibulum id purus lorem.</p>
    </div>
    <div class="signature">
      <p class="name">Rosalind Merriweather</p>
      <p class="role">Co-Founder &amp; CEO</p>
    </div>
    <footer class="footer-band">LAW OFFICES OF HARLAN B. WHITCOMBE</footer>
  </section>

  <section class="sheet sheet--cover">
    <div class="crest-large" role="img" aria-label="Family crest with helmet and mantling"></div>
    <p class="cover-firm">LAW OFFICES OF HARLAN B. WHITCOMBE</p>
  </section>
</body>
</html>
```